Business Card Design

We would like a business card that utilizes our current logo and keeps with the same feel - elegant and organic. Our farm isn't about mass production, it's about excellence, education, beautiful events and flowers - people, culture, and community.

Target Market(s)

Patrons to our farm who are interested in weddings, events, or our flowers and vegetables.

Contact Information for Business Card

Name, address, cell email (Danielle Hoskins, 2716 Wrenfield Rd, Brookvale, CO 80519, cell 30.412.6638, email danielle@wrenfieldacres.com)

```html
<!DOCTYPE html>
<html lang="en">
<head>
<meta charset="utf-8">
<title>Wrenfield Acres – Business Card</title>
<link rel="stylesheet" href="https://fonts.googleapis.com/css2?family=Dancing+Script:wght@600&family=Open+Sans:wght@400&display=swap">
<style>
  :root {
    --page: #ffffff;
    --card-front: #ffffff;
    --sage: #778a77;
    --sage-light: #879786;
    --leaf-faint: #f3f3f3;
    --icon-dark: #4a4a4a;
    --ink: #444444;
    --white: #ffffff;
  }
  * { margin: 0; padding: 0; box-sizing: border-box; }
  html, body { width: 1200px; height: 1200px; overflow: hidden; background: var(--page); }
  body { position: relative; font-family: "Open Sans", Arial, sans-serif; }

  .card {
    position: absolute; left: 178px; width: 844px; height: 516px;
    box-shadow: 0 2px 8px rgba(0,0,0,0.18); overflow: hidden;
  }
  .card--front { top: 64px; background: var(--card-front); }
  .card--back { top: 620px; background: var(--sage); }

  .leaf-band { position: absolute; left: 0; right: 0; bottom: 0; }
  .card--front .leaf-band { height: 120px; background: linear-gradient(to bottom, rgba(243,243,243,0), var(--leaf-faint) 45%); }
  .card--back .leaf-band { height: 148px; background: linear-gradient(to bottom, rgba(135,151,134,0), var(--sage-light) 50%, rgba(135,151,134,0.7)); }

  .brand {
    position: absolute; white-space: nowrap;
    font-family: "Open Sans", Arial, sans-serif; font-weight: 400;
    display: flex; align-items: center; gap: 12px;
  }
  .brand__dot { width: 14px; height: 14px; border-radius: 50%; }
  .card--front .brand { left: 222px; top: 268px; transform: translate(-50%, -50%); font-size: 40px; color: var(--sage); }
  .card--front .brand__dot { background: var(--sage); }
  .card--back .brand { left: 422px; top: 226px; transform: translate(-50%, -50%); font-size: 56px; color: var(--white); }
  .card--back .brand__dot { background: var(--white); width: 18px; height: 18px; }

  .divider { position: absolute; left: 421px; top: 65px; width: 2px; height: 407px; background: var(--sage); }

  .person { position: absolute; left: 462px; top: 82px; width: 330px; }
  .person__name {
    font-family: "Dancing Script", cursive; font-weight: 600; font-size: 53px;
    color: var(--sage); line-height: 1; padding-bottom: 2px;
    border-bottom: 2px solid var(--sage); white-space: nowrap;
  }
  .person__role { text-align: right; font-size: 31px; color: var(--ink); line-height: 1.1; padding-right: 8px; }

  .contact { position: absolute; left: 464px; top: 265px; list-style: none; }
  .contact__item { display: flex; align-items: center; height: 52px; margin-bottom: 16px; }
  .contact__icon { width: 52px; height: 52px; flex: none; margin-right: 20px; }
  .contact__text { font-size: 21px; color: var(--ink); line-height: 1.45; white-space: nowrap; }
</style>
</head>
<body>
  <section class="card card--front">
    <div class="leaf-band" role="img" aria-label="Faint scattered leaf pattern along the bottom edge"></div>
    <div class="brand"><span class="brand__dot"></span>Wrenfield Acres</div>
    <div class="divider"></div>
    <div class="person">
      <p class="person__name">Danielle Hoskins</p>
      <p class="person__role">Owner</p>
    </div>
    <ul class="contact">
      <li class="contact__item">
        <svg class="contact__icon" viewBox="0 0 52 52" aria-hidden="true">
          <circle cx="26" cy="26" r="26" fill="var(--icon-dark)"/>
          <path d="M13 26 L26 14 L39 26" fill="none" stroke="#fff" stroke-width="3.5" stroke-linejoin="round"/>
          <path d="M17 25 V38 H23 V31 H29 V38 H35 V25 L26 17 Z" fill="#fff"/>
        </svg>
        <span class="contact__text">2716 Wrenfield Rd,<br>Brookvale, CO 80519,</span>
      </li>
      <li class="contact__item">
        <svg class="contact__icon" viewBox="0 0 52 52" aria-hidden="true">
          <circle cx="26" cy="26" r="26" fill="var(--icon-dark)"/>
          <path d="M14 16 L40 27 L26 30 L23 40 Z" fill="#fff"/>
          <path d="M26 30 L40 27" stroke="var(--icon-dark)" stroke-width="1.5"/>
        </svg>
        <span class="contact__text">30.412.6638,</span>
      </li>
      <li class="contact__item">
        <svg class="contact__icon" viewBox="0 0 52 52" aria-hidden="true">
          <circle cx="26" cy="26" r="26" fill="var(--icon-dark)"/>
          <path d="M12 22 Q26 12 40 22 L37 26 L32 24 L32 21 Q26 19 20 21 L20 24 L15 26 Z" fill="#fff"/>
          <rect x="16" y="26" width="20" height="12" rx="2" fill="#fff"/>
          <circle cx="26" cy="32" r="3.5" fill="var(--icon-dark)"/>
        </svg>
        <span class="contact__text">danielle@wrenfieldacres.com</span>
      </li>
    </ul>
  </section>

  <section class="card card--back">
    <div class="leaf-band" role="img" aria-label="Soft leaf pattern along the bottom edge"></div>
    <div class="brand"><span class="brand__dot"></span>Wrenfield Acres</div>
  </section>
</body>
</html>
```